Corporate Design für eine Beratungsfirma in der Finanzindustrie gesucht
The design is excellent and we are 100% satisfied. We got all the file formats we wanted to have and brezzolino gave us every help we needed, after the project was finished. The collaboration was very pleasant.
Zielgruppe
IT Beratung und Softwarelösungen für die Finanzindustrie. Wir bewegen uns ausschliesslich im B2B Bereich (Entscheiderebene).
siehe der Entwurf unserer Homepage: http://71230548.kvx.nordhost-server.eu/index-lumavo.html
Aufgabenstellung
Da unsere Zielgruppe eher konservativ ist, legen wir großen Wert auf Schlichtheit und Seriosität im Design. Die Farben sollten eher ruhig gehalten sein.

```html
<!DOCTYPE html>
<html lang="de">
<head>
<meta charset="utf-8">
<title>Lumavo – Geschäftsangaben</title>
<link rel="stylesheet" href="https://fonts.googleapis.com/css2?family=Raleway:wght@200;300&display=swap">
<style>
  :root {
    --paper: #ffffff;
    --ink: #1d1d1b;
    --ink-soft: #4a4a48;
    --icon-grey: #5a5a5a;
    --card-bg: #232323;
    --card-text: #e6e6e6;
    --card-muted: #bdbdbd;
    --fold-mark: #1d1d1b;
  }
  * { margin: 0; padding: 0; box-sizing: border-box; }
  html, body { width: 849px; height: 1200px; overflow: hidden; background: var(--paper); }
  body { position: relative; font-family: "Raleway", "Helvetica Neue", Arial, sans-serif; color: var(--ink); font-weight: 300; }

  .sender-line { position: absolute; left: 82px; top: 114px; font-size: 12.5px; line-height: 17px; color: var(--ink-soft); }

  .letterhead { position: absolute; left: 540px; top: 88px; width: 242px; }
  .brand { display: flex; align-items: center; justify-content: flex-end; gap: 14px; }
  .brand-dot { width: 34px; height: 34px; border: 2px solid var(--ink); border-radius: 50%; }
  .brand-name { font-size: 56px; font-weight: 200; letter-spacing: 5px; line-height: 1; }

  .address { position: absolute; left: 593px; top: 158px; font-size: 17.5px; line-height: 24px; letter-spacing: 1.6px; }
  .contact { position: absolute; left: 564px; top: 253px; font-size: 17.5px; line-height: 24.5px; letter-spacing: 1.8px; }
  .contact-row { display: flex; align-items: center; gap: 11px; }
  .contact-icon { width: 17px; height: 17px; flex: none; }

  .fold-mark { position: absolute; left: 0; width: 25px; height: 1px; background: var(--fold-mark); }
  .fold-mark.top { top: 352px; }
  .fold-mark.middle { top: 600px; }
  .fold-mark.punch { top: 775px; }

  .business-card { position: absolute; left: 238px; top: 475px; width: 222px; height: 344px; background: var(--card-bg); color: var(--card-text); }
  .card-brand { position: absolute; left: 34px; top: 36px; display: flex; align-items: center; gap: 8px; }
  .card-brand .brand-dot { width: 18px; height: 18px; border: 1.5px solid var(--card-text); }
  .card-brand .brand-name { font-size: 30px; letter-spacing: 2.5px; }
  .card-person { position: absolute; left: 80px; top: 104px; }
  .person-name { font-size: 13.5px; line-height: 16px; }
  .person-role { font-size: 9.5px; letter-spacing: 1px; color: var(--card-muted); }
  .card-address { position: absolute; left: 80px; top: 214px; font-size: 9.5px; line-height: 13.7px; letter-spacing: 1px; }
  .card-contact { position: absolute; left: 64px; top: 269px; font-size: 9.5px; line-height: 14px; letter-spacing: 1.1px; }
  .card-contact .contact-row { gap: 5px; }
  .card-contact .contact-icon { width: 11px; height: 11px; }

  .page-label { position: absolute; left: 86px; top: 1128px; font-size: 12.5px; color: var(--ink-soft); }
</style>
</head>
<body>
  <svg width="0" height="0" style="position:absolute" aria-hidden="true">
    <defs>
      <symbol id="icon-phone" viewBox="0 0 20 20">
        <circle cx="10" cy="10" r="10" fill="currentColor"/>
        <path d="M5 8.5c0-2 2.2-3 5-3s5 1 5 3l-1.8.6-.6-1.6c-1.7-.5-3.5-.5-5.2 0l-.6 1.6z" fill="#fff"/>
        <rect x="6.5" y="10" width="7" height="4.5" rx="1" fill="#fff"/>
      </symbol>
      <symbol id="icon-fax" viewBox="0 0 20 20">
        <circle cx="10" cy="10" r="10" fill="currentColor"/>
        <rect x="4.5" y="7" width="11" height="5" rx="1" fill="#fff"/>
        <rect x="7" y="10.5" width="6" height="4.5" fill="#fff" stroke="currentColor" stroke-width="1"/>
        <rect x="7" y="4.5" width="6" height="2.5" fill="#fff"/>
      </symbol>
      <symbol id="icon-mail" viewBox="0 0 20 20">
        <circle cx="10" cy="10" r="10" fill="currentColor"/>
        <rect x="5" y="6.5" width="10" height="7" fill="none" stroke="#fff" stroke-width="1.2"/>
        <path d="M5 6.5l5 4 5-4M5 13.5l3.6-3.3M15 13.5l-3.6-3.3" fill="none" stroke="#fff" stroke-width="1.2"/>
      </symbol>
    </defs>
  </svg>

  <div class="sender-line">Lumavo GmbH<br>Lindenhofweg 7 - D-65432 Talheim</div>

  <header class="letterhead">
    <div class="brand"><span class="brand-dot"></span><span class="brand-name">Lumavo</span></div>
  </header>
  <div class="address">Lumavo GmbH<br>Lindenhofweg 7<br>D-65432 Talheim</div>
  <div class="contact" style="color:var(--icon-grey)">
    <div class="contact-row"><svg class="contact-icon"><use href="#icon-phone"/></svg><span style="color:var(--ink)">(00 00) 00 00 00</span></div>
    <div class="contact-row"><svg class="contact-icon"><use href="#icon-fax"/></svg><span style="color:var(--ink)">(00 00) 00 00 00</span></div>
    <div class="contact-row"><svg class="contact-icon"><use href="#icon-mail"/></svg><span style="color:var(--ink)">contact@lumavo.de</span></div>
  </div>

  <span class="fold-mark top"></span>
  <span class="fold-mark middle"></span>
  <span class="fold-mark punch"></span>

  <section class="business-card">
    <div class="card-brand"><span class="brand-dot"></span><span class="brand-name">Lumavo</span></div>
    <div class="card-person">
      <div class="person-name">Tobias Merkfeld</div>
      <div class="person-role">Founder</div>
    </div>
    <div class="card-address">Lumavo GmbH<br>Lindenhofweg 7<br>D-65432 Talheim</div>
    <div class="card-contact" style="color:var(--card-text)">
      <div class="contact-row"><svg class="contact-icon" style="color:#fff"><use href="#icon-phone"/></svg><span>(00 00) 00 00 00</span></div>
      <div class="contact-row"><svg class="contact-icon" style="color:#fff"><use href="#icon-fax"/></svg><span>(00 00) 00 00 00</span></div>
      <div class="contact-row"><svg class="contact-icon" style="color:#fff"><use href="#icon-mail"/></svg><span>contact@lumavo.de</span></div>
    </div>
  </section>

  <div class="page-label">Geschäftsangaben</div>
</body>
</html>
```